Fresh Nest Builder Guide needs a new Landing Page

I like to get a landing page or website with 2-3 pages to help target home buyers who are looking to buy homes from builders such as PV Dwellings, Moritz, G.T. Falwick, etc. The landing page/website to be non-cluttered and be able to explain to home buyers that there are many benefits to include me as their buyer's agent when they buy a brand new home from any builders.
I may want to incorporate a short explanation video (animated) on the landing page and then for the viewer to click on a button that will take them to another page where they can search for new homes from different builders.
Target Market(s)
Home buyers looking to buy brand new home from builders such as PV Dwellings, Moritz, G.T. Falwick, etc.
Industry/Entity Type
Real Estate
Number of Pages Required
2 page
Requirements
Must have
- The landing page may have the explanation video at the bottom of the landing page (scrolled down) or there may be a CALL TO ACTION button that takes the viewer to the 2nd page to watch the explanation video. Once they watched the explanation video and are still interested, they can click on another CALL TO ACTION button that will take them to another website that they will be able to search for all the available new homes and register their contact information.
Should not have
- No clutters and no dark colors.

```html
<!DOCTYPE html>
<html lang="en">
<head>
<meta charset="utf-8">
<title>Fresh Nest Builder Guide</title>
<link href="https://fonts.googleapis.com/css2?family=Open+Sans:wght@400;600;700&family=Philosopher&display=swap" rel="stylesheet">
<style>
:root{
  --brown:#a0714a;
  --brown-btn:#8b5a32;
  --dark:#2e2016;
  --footer:#3f3429;
  --footer-line:#5a4e43;
  --text:#5b5b5b;
  --heading:#2a2118;
  --white:#ffffff;
}
*{margin:0;padding:0;box-sizing:border-box}
html,body{width:923px;height:1200px;overflow:hidden}
body{position:relative;font-family:'Open Sans',sans-serif;background:var(--white);color:var(--text)}
.abs{position:absolute}
.topbar{left:0;top:0;width:923px;height:16px;background:var(--brown);color:var(--white);font-size:7.5px}
.topbar .phone{left:144px;top:3px;display:flex;align-items:center;gap:5px}
.topbar .mail{left:630px;top:3px;display:flex;align-items:center;gap:5px}
.header{left:0;top:16px;width:923px;height:51px;border-bottom:1px solid #6b5444}
.brand{left:142px;top:14px;display:flex;align-items:center;gap:5px;font-family:'Open Sans',sans-serif;font-weight:600;font-size:12px;color:var(--dark);line-height:1.1}
.brand .dot{width:10px;height:10px;border-radius:50%;background:var(--brown)}
.nav{left:306px;top:22px;display:flex;gap:19px;font-size:10.5px;color:#3e3e3e}
.search{left:615px;top:17px;width:170px;height:21px;border:1px solid #6b5444;display:flex}
.search span{flex:1;font-size:8.5px;padding:4px 6px;color:#555}
.search i{width:25px;border-left:1px solid #6b5444;display:flex;align-items:center;justify-content:center}
.hero{left:0;top:67px;width:923px;height:315px;background:linear-gradient(180deg,#4a4e58 0%,#7d6d5a 45%,#5a4a3a 75%,#3a3128 100%)}
.hero h1{left:144px;top:82px;width:360px;font-family:'Philosopher',sans-serif;font-weight:400;font-size:22px;line-height:24px;color:var(--white);text-shadow:0 1px 3px rgba(0,0,0,.6)}
.form{left:606px;top:23px;width:216px;height:292px;background:var(--dark);padding:0 13px}
.form h2{text-align:center;font-size:11.5px;font-weight:700;color:var(--white);margin:29px 0 14px}
.field{background:var(--white);height:26px;margin:0 2px 8px;font-size:10px;color:#333;padding:8px 12px 0}
.field.msg{height:71px}
.send{margin-top:10px;height:24px;background:var(--brown-btn);color:var(--white);font-size:11px;text-align:center;line-height:24px}
.intro{left:0;top:382px;width:923px;height:265px;background:linear-gradient(180deg,#fff 0%,#fff 35%,#e9e9e9 70%,#dcdcdc 100%);text-align:center}
.intro h2{font-family:'Philosopher',sans-serif;font-weight:400;font-size:20.5px;color:var(--heading);margin-top:22px}
.intro h3{font-family:'Philosopher',sans-serif;font-weight:400;font-size:17px;color:var(--heading);margin-top:3px}
.rule{height:1px;background:var(--brown);margin:6px auto 0}
.intro p{font-size:10.5px;line-height:15.4px;margin:0 auto}
.video-title{left:0;top:651px;width:923px;text-align:center;font-family:'Philosopher',sans-serif;font-size:18px;color:var(--heading)}
.video{left:284px;top:697px;width:356px;height:208px;background:linear-gradient(180deg,#6d7884 0%,#77695a 45%,#4e3d2e 75%,#3c4a2c 100%);box-shadow:0 3px 6px rgba(0,0,0,.25)}
.more{left:390px;top:920px;width:148px;height:31px;background:var(--brown-btn);color:var(--white);font-size:11.5px;text-align:center;line-height:31px}
.footer{left:0;top:970px;width:923px;height:230px;background:var(--footer);color:var(--white)}
.footer h4{position:absolute;top:33px;font-size:13px;font-weight:400;letter-spacing:.2px}
.footer h4::after{content:"";display:block;width:38px;height:1px;background:#d9d0c6;margin-top:6px}
.footer .col{position:absolute;top:72px;font-size:11px;line-height:13.6px}
.links div{margin-bottom:6.6px}
.contact td{vertical-align:top;padding-bottom:6px}
.copy{left:0;top:1177px;width:923px;height:23px;border-top:1px solid var(--footer-line);text-align:center;font-size:8.5px;line-height:22px;color:var(--white);background:var(--footer)}
</style>
</head>
<body>
<div class="abs topbar">
  <div class="abs phone"><svg width="7" height="8" viewBox="0 0 7 8"><path d="M1.5 0.5 L3 2.2 L2.2 3.2 Q3 5 4.5 5.8 L5.4 5 L6.8 6.5 L5.8 7.6 Q1 6.5 0.4 1.5 Z" fill="#fff"/></svg>555.010.4421</div>
  <div class="abs mail"><svg width="10" height="7" viewBox="0 0 10 7"><rect x="0.5" y="0.5" width="9" height="6" fill="none" stroke="#fff"/><path d="M0.5 0.5 L5 4 L9.5 0.5" fill="none" stroke="#fff"/></svg>hello@freshnestguide.com</div>
</div>

<header class="abs header">
  <div class="abs brand"><span class="dot"></span><span>Fresh Nest<br>Builder Guide</span></div>
  <nav class="abs nav"><span>NEW HOME</span><span>REGISTER</span><span>CONTACT INFORMATION</span></nav>
  <div class="abs search"><span>Search</span><i><svg width="8" height="8" viewBox="0 0 8 8"><circle cx="3.2" cy="3.2" r="2.4" fill="none" stroke="#333" stroke-width="1.1"/><path d="M5 5 L7.5 7.5" stroke="#333" stroke-width="1.2"/></svg></i></div>
</header>

<section class="abs hero" role="img" aria-label="Large two-storey stone house with lit windows at dusk">
  <h1 class="abs">Home is a shelter from storms-all sorts of storms.</h1>
  <div class="abs form">
    <h2>REGISTER FORM</h2>
    <div class="field">Name</div>
    <div class="field">Email</div>
    <div class="field">Phone no</div>
    <div class="field msg">Message</div>
    <div class="send">Sent</div>
  </div>
</section>

<section class="abs intro">
  <h2>There is nothing more important than a good, safe, secure home</h2>
  <h3>How to buy your new home</h3>
  <div class="rule" style="width:124px"></div>
  <p style="width:550px;margin-top:17px">A home, or domicile, is a living space used as a permanent or semi-permanent residence for an individual, family, household or several families in a tribe. It is often a house, apartment, or other building, or alternatively a mobile home, houseboat, yurt or any other portable shelter. A principle of constitutional law in many countries, related to the right to privacy enshrined in article 12 of the Universal Declaration of Human Rights[1] is the inviolability of the home as an individual's place of shelter and refuge.</p>
  <p style="width:625px;margin-top:13px">Homes typically provide areas and facilities for sleeping, preparing food, eating and hygiene. Larger groups may live in a nursing home, children's home, convent or any similar institution. A homestead also includes agricultural land and facilities for domesticated animals.</p>
</section>

<div class="abs video-title">OUR VEDIO<div class="rule" style="width:72px;margin-top:4px"></div></div>
<div class="abs video" role="img" aria-label="Modern house with wooden deck at dusk, video thumbnail">
  <svg class="abs" style="left:166px;top:90px" width="30" height="32" viewBox="0 0 30 32"><path d="M2 2 L28 16 L2 30 Z" fill="#fff" stroke="#fff" stroke-width="3" stroke-linejoin="round"/></svg>
</div>
<div class="abs more">More Vedios</div>

<footer class="abs footer">
  <h4 style="left:106px">ABOUT NEW HOME</h4>
  <h4 style="left:352px">BUILDERS</h4>
  <h4 style="left:450px">PROPERTIES</h4>
  <h4 style="left:604px">CONTACT INFORMATION</h4>
  <div class="col" style="left:105px;width:230px">A home, or domicile, is a living space used as a permanent or semi-permanent residence for an individual, family, house hold or several families in a tribe. It is often a house, apartment, or other building, or alternatively a mobile home, houseboat, yurt or any other portable shelter.</div>
  <div class="col links" style="left:354px"><div>PV Dwellings</div><div>Moritz</div><div>G.T. Falwick</div></div>
  <div class="col links" style="left:452px;font-size:10.5px"><div>NEW HOME</div><div>REGISTER</div><div>CONTACT INFORMATION</div></div>
  <table class="col contact" style="left:603px;border-collapse:collapse">
    <tr><td style="width:65px">Phone no</td><td>555.010.4421<br>555.010.7730</td></tr>
    <tr><td>Email</td><td>hello@freshnestguide.com</td></tr>
    <tr><td>Location</td><td>48 Linden Court,&nbsp; FL 30000</td></tr>
  </table>
</footer>
<div class="abs copy">copyright2018freshnestguide</div>
</body>
</html>
```